Wattlebrook Cleaning Tablets needs 4 x labels

We're about to launch a very exciting cleaning product to market and need your help to brand the 4 x bottles. www.wattlebrook.com.au will change the way people buy and use household cleaning products whilst significantly reducing the impact on the earth.

The tablets are dropped into the long life recycled plastic bottle, you simply add water, wait for the tab to dissolve and begin cleaning.

Target Market(s)

Women aged between 30 - 65, care for the environment, want to use less plastic, are early adopters and like to try new things. Care about a clean home and using less chemicals. Want less packaging, less plastic, less carbon emissions.

Industry/Entity Type

House Cleaning

Font styles to use
Sans Serif

Requirements
Must have
• Each label must have an obvious colour differentiator and each label must be identical in it's dimensions and information. Should look uniform when all 4 bottles are aligned in the cupboard. Limited / no images apart from logo.
Nice to have
• Simple, clear, bold, striking. Limited / no pictures. Clean lines with lots of space.
Should not have
• Sparkvane Glass Label must have a strip of blue (hex BAE1FF).
Grease Ranger Kitchen Cleaner must have a strip of colour (FFD6F3)
The Fizzer Bathroom cleaner must have a colour strip hex # FFFFBA
The Allrounder Multip Purpose must have a strip of colour Hex #BAFFC9

```html
<!DOCTYPE html>
<html lang="en">
<head>
<meta charset="utf-8">
<title>Wattlebrook Cleaning Tablets – Label Range</title>
<link rel="stylesheet" href="https://fonts.googleapis.com/css2?family=Bebas+Neue&family=Source+Sans+3:wght@400&family=Source+Serif+4:ital,wght@1,300;1,400&display=swap">
<style>
  :root {
    --page: #ffffff;
    --kraft: #cbb08a;
    --kraft-light: #d6bf9c;
    --ink: #231f20;
    --band-glass: #b5cced;
    --band-kitchen: #fbd9e2;
    --band-bath: #fcf8c6;
    --band-multi: #b2e0cd;
    --accent-glass: #6a8bc2;
    --accent-kitchen: #e597a9;
    --accent-bath: #cdbb5e;
    --accent-multi: #55a88f;
    --label-w: 230px;
    --label-h: 460px;
    --band-top: 247px;
  }
  * { margin: 0; padding: 0; box-sizing: border-box; }
  html, body { width: 1200px; height: 849px; overflow: hidden; background: var(--page); }
  .range {
    width: 1200px; height: 849px;
    display: flex; justify-content: center; align-items: center; gap: 50px;
  }
  .label {
    position: relative;
    width: var(--label-w); height: var(--label-h);
    background: linear-gradient(160deg, var(--kraft-light), var(--kraft));
    overflow: hidden;
  }
  .label__band {
    position: absolute; left: 0; right: 0; top: var(--band-top); bottom: 0;
    background: var(--band);
  }
  .brand {
    position: absolute; left: 0; right: 0; top: 24px;
    text-align: center;
    font-family: "Bebas Neue", sans-serif;
    font-size: 40px; line-height: 1; color: var(--ink);
    letter-spacing: 0.5px;
  }
  .badge {
    position: absolute; left: 130px; top: 111px;
    width: 80px; height: 80px; border-radius: 50%;
    border: 1.5px solid var(--accent); opacity: 0.75;
  }
  .category {
    position: absolute; left: 17px; top: 196px;
    font-family: "Source Serif 4", serif; font-style: italic; font-weight: 300;
    font-size: 14px; line-height: 18px; color: var(--accent);
    white-space: nowrap;
  }
  .product-name {
    position: absolute; left: 16px; top: 218px; right: 10px;
    font-family: "Bebas Neue", sans-serif; font-weight: 400;
    font-size: 48px; line-height: 0.92; color: var(--ink);
    white-space: nowrap;
  }
  .tagline {
    position: absolute; left: 17px; top: 336px;
    list-style: none;
    font-family: "Source Serif 4", serif; font-style: italic; font-weight: 400;
    font-size: 16px; line-height: 22.5px; color: var(--accent);
  }
  .volume {
    position: absolute; right: 6px; bottom: 10px; width: 50px;
    border: 1px solid var(--accent);
    font-family: "Source Sans 3", sans-serif; text-align: center;
  }
  .volume__origin { font-size: 8px; line-height: 11px; color: var(--accent); padding-top: 2px; }
  .volume__rule { display: block; margin: 1px auto; }
  .volume__size {
    border-top: 1px solid var(--accent);
    font-size: 11px; line-height: 15px; color: var(--ink);
  }
  .label--glass   { --band: var(--band-glass);   --accent: var(--accent-glass); }
  .label--kitchen { --band: var(--band-kitchen); --accent: var(--accent-kitchen); }
  .label--bath    { --band: var(--band-bath);    --accent: var(--accent-bath); }
  .label--multi   { --band: var(--band-multi);   --accent: var(--accent-multi); }
</style>
</head>
<body>
<main class="range">

  <article class="label label--glass">
    <div class="label__band"></div>
    <div class="brand">Wattlebrook</div>
    <div class="badge"></div>
    <p class="category">Window Cleaner</p>
    <h2 class="product-name">Sparkvane</h2>
    <ul class="tagline"><li>One Bottle.</li><li>One Tab.</li><li>Dissolve.</li><li>Clean.</li><li>Repeat.</li></ul>
    <div class="volume">
      <div class="volume__origin">Kelpbay
        <svg class="volume__rule" width="26" height="4" viewBox="0 0 26 4"><path d="M1 3 Q13 0 25 3" fill="none" stroke="currentColor" stroke-width="1"/></svg>
        Australia</div>
      <div class="volume__size">500 ml</div>
    </div>
  </article>

  <article class="label label--kitchen">
    <div class="label__band"></div>
    <div class="brand">Wattlebrook</div>
    <div class="badge"></div>
    <p class="category">Kitchen Cleaner</p>
    <h2 class="product-name">Grease<br>Ranger</h2>
    <ul class="tagline"><li>One Bottle.</li><li>One Tab.</li><li>Dissolve.</li><li>Clean.</li><li>Repeat.</li></ul>
    <div class="volume">
      <div class="volume__origin">Kelpbay
        <svg class="volume__rule" width="26" height="4" viewBox="0 0 26 4"><path d="M1 3 Q13 0 25 3" fill="none" stroke="currentColor" stroke-width="1"/></svg>
        Australia</div>
      <div class="volume__size">500 ml</div>
    </div>
  </article>

  <article class="label label--bath">
    <div class="label__band"></div>
    <div class="brand">Wattlebrook</div>
    <div class="badge"></div>
    <p class="category">Bathroom Cleaner</p>
    <h2 class="product-name">The<br>Fizzer</h2>
    <ul class="tagline"><li>One Bottle.</li><li>One Tab.</li><li>Dissolve.</li><li>Clean.</li><li>Repeat.</li></ul>
    <div class="volume">
      <div class="volume__origin">Kelpbay
        <svg class="volume__rule" width="26" height="4" viewBox="0 0 26 4"><path d="M1 3 Q13 0 25 3" fill="none" stroke="currentColor" stroke-width="1"/></svg>
        Australia</div>
      <div class="volume__size">500 ml</div>
    </div>
  </article>

  <article class="label label--multi">
    <div class="label__band"></div>
    <div class="brand">Wattlebrook</div>
    <div class="badge"></div>
    <p class="category">Multi Purpose Cleaner</p>
    <h2 class="product-name">The<br>Allrounder</h2>
    <ul class="tagline"><li>One Bottle.</li><li>One Tab.</li><li>Dissolve.</li><li>Clean.</li><li>Repeat.</li></ul>
    <div class="volume">
      <div class="volume__origin">Kelpbay
        <svg class="volume__rule" width="26" height="4" viewBox="0 0 26 4"><path d="M1 3 Q13 0 25 3" fill="none" stroke="currentColor" stroke-width="1"/></svg>
        Australia</div>
      <div class="volume__size">500 ml</div>
    </div>
  </article>

</main>
</body>
</html>
```